Re-launching marine insurance adjusting company - looking for energy

I am a sole practitioner specializing in the profession of average adjusting. There is an on-line brochure at www.kbrtmarine.example I am one of only a handful of specialists in this field and I enjoy a fair amount of name recognition, domestically in the US and internationally. My principal markets are the US, the London and Scandinavian insurance markets and shipowners and insurers in Latin America.
The business is a mixture of law, accounting and insurance and my clientele relies on a time-sensitive and accurate work-product, clearly stating an insurance company's liability for a given claim. The identity needs to project gravitas rather than flash.
Since 1998 I have traded as "The Halloway Bureau" but have also attempted to establish the name KBRTMARINE.example so that people would visit my website.
I want to implement a single identity across my stationery, business cards and website. I have come to see "The Halloway Bureau" as rather fatuous, since there is no company, it is just me. The Internet domain KBRTMARINE is long-established and I would be reluctant to change it. I have considered trading as simply Marcus T Holloway, MTH, KBRTMARINE or attempting to come up with a name that could be abbreviated to MTH, e.g. M Holloway Tessellate - but I can't find a suitable word for the second S.
Logo-wise, I have considered a stylized MTH or KBRTMARINE redolent of waves of the sea. A nautical theme embodying a cargo ship, navigational beacon or lighthouse might be appropriate but these tend to be hackneyed.
I have attached a card that I mocked up at Zib, connoting stacking up numbers, which I really like, but I think it is too cryptic for people in most insurance companies, who don't particularly think laterally or they wouldn't work in marine insurance, and the card that I use currently, which I intended to be understated, but in fact it states nothing.
I have also attached my current letterhead, to demonstrate how I really need help.
Finally, I have attached a credentials sheet, to attempt to establish how narrow and deep is the professional niche that I occupy.
What I am looking to implement is a single logo, font, them and color scheme to use across my website, letterhead and business cards.
Over to the Pencil Guild...
Ship owners and insurance companies
Accounting

```html
<!DOCTYPE html>
<html lang="en">
<head>
<meta charset="utf-8">
<title>Marcus T. Holloway — Letterhead</title>
<link rel="stylesheet" href="https://fonts.googleapis.com/css2?family=Lato:wght@400;700&display=swap">
<style>
  :root {
    --backdrop: #e3e9ee;
    --paper: #ffffff;
    --parchment-light: #e6d6b6;
    --parchment: #d8c39b;
    --parchment-dark: #c9ae80;
    --sea: #4fb3d6;
    --sea-light: #a9dcec;
    --ink: #1b1712;
    --rope: #9a5a25;
    --anchor-red: #8e1f22;
  }
  * { box-sizing: border-box; margin: 0; padding: 0; }
  html, body {
    width: 1036px;
    height: 1200px;
    overflow: hidden;
    background: var(--backdrop);
    font-family: "Lato", sans-serif;
    color: var(--ink);
  }
  .letterhead {
    position: absolute;
    left: 108px;
    top: 20px;
    width: 820px;
    height: 1160px;
    background: var(--paper);
    box-shadow: 0 2px 6px rgba(0, 0, 0, 0.18);
    overflow: hidden;
  }
  .letterhead__header {
    position: absolute;
    inset: 0 0 auto 0;
    height: 250px;
    background:
      radial-gradient(ellipse at 30% 30%, var(--parchment-light), transparent 60%),
      linear-gradient(180deg, var(--parchment) 0%, var(--parchment-dark) 100%);
  }
  .letterhead__sender {
    position: absolute;
    left: 46px;
    top: 58px;
    font-size: 19px;
    line-height: 1.3;
  }
  .letterhead__sender-name {
    font-weight: 700;
    font-size: 22px;
  }
  .letterhead__brand {
    position: absolute;
    right: 46px;
    top: 56px;
    display: flex;
    align-items: center;
    gap: 14px;
  }
  .letterhead__brand-name {
    font-weight: 700;
    font-size: 40px;
    letter-spacing: 1px;
    color: var(--rope);
  }
  .letterhead__brand-mark {
    width: 40px;
    height: 40px;
    border-radius: 50%;
    background: var(--anchor-red);
  }
  .letterhead__waves {
    position: absolute;
    left: 0;
    right: 0;
    top: 178px;
    height: 72px;
    background: linear-gradient(180deg, var(--sea) 0%, var(--sea) 70%, var(--sea-light) 100%);
  }
  .letterhead__fade {
    position: absolute;
    left: 0;
    right: 0;
    top: 250px;
    height: 30px;
    background: linear-gradient(180deg, rgba(255,255,255,0.6), var(--paper));
  }
  .letterhead__footer {
    position: absolute;
    inset: auto 0 0 0;
    height: 130px;
    background:
      linear-gradient(180deg, var(--paper) 0%, var(--parchment) 35%, var(--parchment-dark) 100%);
    font-size: 18px;
    line-height: 1.3;
  }
  .letterhead__phones {
    position: absolute;
    left: 46px;
    bottom: 28px;
  }
  .letterhead__online {
    position: absolute;
    right: 46px;
    bottom: 48px;
    text-align: left;
  }
</style>
</head>
<body>
  <main class="letterhead">
    <header class="letterhead__header">
      <address class="letterhead__sender" style="font-style: normal;">
        <div class="letterhead__sender-name">Marcus T. Holloway</div>
        <div>48 Harbor Row East,</div>
        <div>Portside, NY 10990, USA</div>
      </address>
      <div class="letterhead__brand">
        <span class="letterhead__brand-name">KBRTMARINE</span>
        <span class="letterhead__brand-mark" aria-hidden="true"></span>
      </div>
      <div class="letterhead__waves" role="img" aria-label="Band of stylised blue sea waves"></div>
    </header>
    <div class="letterhead__fade" aria-hidden="true"></div>

    <footer class="letterhead__footer">
      <div class="letterhead__phones">
        <div>Tel: +1 (555) 410 2736</div>
        <div>Fax: +1 (555) 410 2790</div>
      </div>
      <div class="letterhead__online">
        <div>Web: www.kbrtmarine.example</div>
        <div>Email: info@kbrtmarine.example</div>
      </div>
    </footer>
  </main>
</body>
</html>
```